Promotional Flyer/Email Design - Cabling services for Broadcast and Audio Visual

We need a promotional flyer/email design to help launch our company, Velcor Lane. We provide cabling services for Broadcast Television and Audio Visual systems. Recent projects include major television events such as the Harrowmere Racquet Classic and Audio Visual/Entertainment systems for wealthy clients in their homes and on-board super yachts.

The flyer will be printed as single sided A5 and also be sent out in the body of a promotional email. It should feature the company logo along with a complementary colour scheme. It should have a clean finish with images that show the type of work we do (cabling and equipment installation) or the setting for these systems (tv studio, super yacht, cinema room, meeting room with projector etc.)

Services we offer are:

Broadcast/AV system design
On-site installation
Rack building
Pre-fabricated cable looms
Fibre optic installation

About the company:

Velcor Lane provide cabling services for Broadcast Television and Audio Visual systems. With over 15 years experience working in these industries we can help with every aspect of design, project managment, installation and maintenance. Our projects range from fibre optic cabling at major sports events to installing and commisioning bespoke control systems on some of the worlds largest super yachts.

Contact details:

To get a quote or discuss your project contact us now
Telephone: TBC
Email: info@velcor-lane.com
Website: www.velcor-lane.com
Address: TBC

Other information:

The company is based in London, UK. Our projects often take place in other countries with work taking place accross Europe and beyond.

We have a London based workshop for rack building and cable pre-fabrication.

Our website is www.velcor-lane.com

Images:

Images attached can be editted for use on the flyer or have ideas taken from them. Only the company logo is required to feature on the final design.

Target Market(s)

Business to business

Industry/Entity Type

It Company

Font styles to use
Sans Serif

Requirements
Must have
• Company logo
• List of services
• Contact details
Nice to have
• Image of cabling, home cinema room, super yacht, luxury home, outside broadcast truck, fibre optic equipment or cabling.

```html
<!DOCTYPE html>
<html lang="en">
<head>
<meta charset="utf-8">
<title>Velcor Lane – Newsletter</title>
<link href="https://fonts.googleapis.com/css2?family=Raleway:wght@300;400;500;600;700&display=swap" rel="stylesheet">
<style>
  :root {
    --stage: #c9c9cb;
    --accent: #e0073c;
    --ink: #2b2b2b;
    --body-text: #555;
    --bar-dark: #2a2a2b;
    --footer-dark: #222224;
    --footer-black: #0b0b0b;
    --panel-left: #d6dce1;
    --panel-right: #e7ecef;
    --quote-btn: #6e6e70;
    --frame: #d4d4d4;
  }
  * { box-sizing: border-box; margin: 0; padding: 0; }
  html, body { width: 1200px; height: 1200px; overflow: hidden; }
  body {
    background: var(--stage);
    font-family: "Raleway", sans-serif;
    position: relative;
  }
  .newsletter {
    position: absolute;
    left: 0; top: 0;
    width: 581px; height: 1373px;
    background: #fff;
    transform-origin: 0 0;
    transform: translate(368px, 51px) scale(0.8);
    box-shadow: 0 8px 40px rgba(0,0,0,.25);
  }
  .newsletter > * { position: absolute; left: 0; width: 581px; }

  .browser-bar {
    top: 0; height: 27px;
    background: var(--bar-dark);
    color: #fff; font-size: 11px; letter-spacing: -.2px;
    display: flex; align-items: center; justify-content: center; gap: 4px;
  }
  .browser-bar a { color: var(--accent); text-decoration: none; font-weight: 300; }

  .masthead { top: 27px; height: 100px; }
  .brand {
    position: absolute; left: 27px; top: 36px;
    display: flex; align-items: center; gap: 10px;
  }
  .brand-mark { width: 22px; height: 22px; background: var(--accent); }
  .brand-name { font-size: 26px; font-weight: 500; color: var(--ink); letter-spacing: -.3px; }
  .social {
    position: absolute; right: 20px; top: 39px;
    display: flex; gap: 5px;
  }
  .social span {
    width: 24px; height: 24px; border-radius: 50%; background: var(--accent);
    display: flex; align-items: center; justify-content: center;
  }
  .social svg { width: 12px; height: 12px; }

  .hero {
    top: 127px; height: 311px;
    background: linear-gradient(180deg, #3d3f45 0%, #6f7176 18%, #a9a9ab 34%, #d8d5cc 46%, #ece9e1 58%, #bcbab6 72%, #d9d9d8 86%, #9e9ea0 100%);
  }
  .label {
    position: absolute;
    background: var(--accent); color: #fff;
    font-weight: 600; text-transform: uppercase;
    padding: 0 7px; line-height: 27px; font-size: 20px; letter-spacing: -.3px;
  }
  .hero .label { left: 25px; bottom: 0; padding: 0 12px; }

  .about {
    top: 453px; padding: 0 20px 0 18px;
    font-size: 13.3px; line-height: 19px; font-weight: 400; color: var(--body-text);
    letter-spacing: -.15px; text-align: justify;
  }

  .photo-pair { top: 565px; height: 192px; }
  .photo-pair .photo { position: absolute; top: 0; width: 262px; height: 192px; border: 1px solid var(--frame); }
  .photo.lounge { left: 19px; background: linear-gradient(100deg, #6f655b 0%, #a39583 30%, #cdbfa9 55%, #b3a48f 75%, #5f544a 100%); }
  .photo.cinema { left: 300px; background: linear-gradient(180deg, #5a4e47 0%, #8f8176 18%, #e6e2da 40%, #d3cfc7 55%, #7c6e64 75%, #4a3e38 100%); }

  .services { top: 770px; height: 201px; }
  .services .about-more {
    position: absolute; left: 0; top: 0; width: 299px; height: 201px;
    background: var(--panel-left);
    padding: 40px 22px 0 19px;
    font-size: 13.3px; line-height: 19px; color: #444; letter-spacing: -.25px;
  }
  .services .about-more p + p { margin-top: 14px; text-align: justify; }
  .services .offer {
    position: absolute; left: 299px; top: 0; width: 282px; height: 201px;
    background: var(--panel-right);
  }
  .offer .label { left: 39px; top: 0; }
  .offer ul { position: absolute; left: 38px; top: 35px; list-style: none; }
  .offer li { font-size: 14px; font-weight: 600; color: var(--ink); line-height: 28px; }

  .gallery { top: 971px; height: 233px; }
  .gallery .label { left: 148px; top: 0; }
  .thumbs { position: absolute; left: 19px; top: 37px; display: flex; gap: 5px; }
  .thumb { width: 86px; }
  .thumb .shot { height: 170px; border: 1px solid var(--frame); }
  .thumb figcaption { font-size: 10px; color: #666; margin-top: 3px; margin-left: -2px; }
  .shot.t1 { background: linear-gradient(180deg, #2d3a34, #5f7368 25%, #3a4a42 50%, #6d7e72 75%, #2e3833); }
  .shot.t2 { background: linear-gradient(180deg, #d4d6d7, #b7bcc0 45%, #8c94a0 70%, #3d4c7a 88%, #c9cbcc); }
  .shot.t3 { background: linear-gradient(180deg, #ececea, #d7d9dc 40%, #c7cad0 60%, #2a3563 85%, #e0e0de); }
  .shot.t4 { background: linear-gradient(180deg, #1f2422, #345a48 30%, #2a2f2d 55%, #3f6a55 80%, #1f2422); }
  .shot.t5 { background: linear-gradient(90deg, #8a8f93, #1c2024 30%, #2a2e32 70%, #5a5e62); }
  .shot.t6 { background: linear-gradient(180deg, #2a2523, #2f6b58 35%, #3a2f2c 60%, #7a4238 85%, #2a2523); }

  .contact {
    top: 1204px; height: 113px;
    background: var(--footer-dark);
    color: #bbb; font-size: 12px; letter-spacing: -.2px;
  }
  .quote {
    position: absolute; left: 112px; top: 2px; width: 369px; height: 23px;
    background: var(--quote-btn); color: #fff;
    font-size: 14px; text-align: center; line-height: 23px;
  }
  .contact-line { position: absolute; display: flex; align-items: center; gap: 5px; }
  .contact-line svg { width: 19px; height: 19px; }
  .phone { font-family: Arial, sans-serif; letter-spacing: 0; }
  .copyright { position: absolute; top: 93px; width: 100%; text-align: center; color: #6d6d6f; font-size: 12px; }

  .legal {
    top: 1317px; height: 56px;
    background: var(--footer-black);
    color: #a5a5a5; font-size: 10px; line-height: 17px; text-align: center;
    padding-top: 10px;
  }
  .legal a { color: #c9c9c9; }
</style>
</head>
<body>
<article class="newsletter">
  <div class="browser-bar">E-mail not displayed correctly? <a href="#">View it in your browser.</a></div>

  <header class="masthead">
    <div class="brand"><span class="brand-mark"></span><span class="brand-name">Velcor Lane</span></div>
    <nav class="social" aria-label="Social links">
      <span><svg viewBox="0 0 12 12"><circle cx="6" cy="6" r="2.4" fill="#fff"/></svg></span>
      <span><svg viewBox="0 0 12 12"><circle cx="6" cy="6" r="2.4" fill="#fff"/></svg></span>
      <span><svg viewBox="0 0 12 12"><circle cx="6" cy="6" r="2.4" fill="#fff"/></svg></span>
      <span><svg viewBox="0 0 12 12"><circle cx="6" cy="6" r="2.4" fill="#fff"/></svg></span>
      <span><svg viewBox="0 0 12 12"><circle cx="6" cy="6" r="2.4" fill="#fff"/></svg></span>
      <span><svg viewBox="0 0 12 12"><circle cx="6" cy="6" r="2.4" fill="#fff"/></svg></span>
    </nav>
  </header>

  <section class="hero" role="img" aria-label="Bright empty television studio with gallery level and a colour-bar screen">
    <h2 class="label">About us</h2>
  </section>

  <p class="about">Velcor Lane provide cabling services for Broadcast Television and Audio Visual systems. With over 15 years experience working in these industries we can help with every aspect of design, project managment, installation and maintenance. Our projects range from fibre optic cabling at major sports events to installing and commisioning bespoke control systems on some of the worlds largest super yachts.</p>

  <div class="photo-pair">
    <div class="photo lounge" role="img" aria-label="Luxury living room with wall-mounted television"></div>
    <div class="photo cinema" role="img" aria-label="Private home cinema room with projection screen"></div>
  </div>

  <section class="services">
    <div class="about-more">
      <p>The company is based in London, UK. Our projects often take place in other countries with work taking place accross Europe and beyond.</p>
      <p>We have a London based workshop for rack building and cable pre-fabrication.</p>
    </div>
    <div class="offer">
      <h2 class="label">Our services:</h2>
      <ul>
        <li>Broadcast/AV system design</li>
        <li>On-site installation</li>
        <li>Rack building</li>
        <li>Pre-fabricated cable looms</li>
        <li>Fibre optic installation</li>
      </ul>
    </div>
  </section>

  <section class="gallery">
    <h2 class="label">Take a look at our gallery</h2>
    <div class="thumbs">
      <figure class="thumb"><div class="shot t1" role="img" aria-label="Patch panels with cabling"></div><figcaption>Image Title</figcaption></figure>
      <figure class="thumb"><div class="shot t2" role="img" aria-label="Cable tray installation"></div><figcaption>Image Title</figcaption></figure>
      <figure class="thumb"><div class="shot t3" role="img" aria-label="Wall-mounted distribution unit"></div><figcaption>Image Title</figcaption></figure>
      <figure class="thumb"><div class="shot t4" role="img" aria-label="Equipment rack with green cabling"></div><figcaption>Image Title</figcaption></figure>
      <figure class="thumb"><div class="shot t5" role="img" aria-label="Black server rack"></div><figcaption>Image Title</figcaption></figure>
      <figure class="thumb"><div class="shot t6" role="img" aria-label="Rack back with cable looms"></div><figcaption>Image Title</figcaption></figure>
    </div>
  </section>

  <footer class="contact">
    <div class="quote">To get a quote or discuss your project contact us now</div>
    <div class="contact-line" style="left:40px;top:33px">
      <svg viewBox="0 0 20 20"><circle cx="10" cy="10" r="9" fill="none" stroke="#e0073c" stroke-width="1.2"/><path d="M5.5 10 10 6l4.5 4M7 9.5V14h6V9.5" fill="none" stroke="#e0073c" stroke-width="1.3"/></svg>
      <span>Your Address will go here Your Address will go here</span>
    </div>
    <div class="contact-line" style="left:40px;top:62px">
      <svg viewBox="0 0 20 20"><circle cx="10" cy="10" r="9" fill="none" stroke="#e0073c" stroke-width="1.2"/><rect x="5.5" y="7" width="9" height="6.5" fill="none" stroke="#e0073c" stroke-width="1.2"/><path d="M5.5 7 10 11l4.5-4" fill="none" stroke="#e0073c" stroke-width="1.2"/></svg>
      <span>info@velcor-lane.com</span>
    </div>
    <div class="contact-line" style="left:231px;top:62px">
      <svg viewBox="0 0 20 20"><circle cx="10" cy="10" r="9" fill="none" stroke="#e0073c" stroke-width="1.2"/><circle cx="10" cy="10" r="4.5" fill="none" stroke="#e0073c" stroke-width="1.2"/><path d="M5.5 10h9M10 5.5c-2 3-2 6 0 9M10 5.5c2 3 2 6 0 9" fill="none" stroke="#e0073c" stroke-width="1"/></svg>
      <span>www.velcor-lane.com</span>
    </div>
    <div class="contact-line" style="left:421px;top:62px">
      <svg viewBox="0 0 20 20"><circle cx="10" cy="10" r="9" fill="none" stroke="#e0073c" stroke-width="1.2"/><path d="M7 5.5c-1.5 1-1.5 3 .5 5.5s4.5 3.5 5.5 2l.5-1-2-1.5-1 .8c-1-.5-2-1.5-2.5-2.5l.8-1L7.5 5.5z" fill="#e0073c"/></svg>
      <span class="phone">07700 900 418</span>
    </div>
    <p class="copyright">Copyright © 2017 Velcor Lane</p>
  </footer>

  <div class="legal">
    <p>You're receiving this newsletter because you bought templates from us.</p>
    <p>Not interested anymore? <a href="#">Unsubscribe</a> Instantly.</p>
  </div>
</article>
</body>
</html>
```